Poster for our office

Looking to get a large print or poster for our office. That has our logo; our core mission; and examples of feedback from clients all on the one print.
Is this something you do?
If so, you’ll see most of the content on our website: pkrt.com.au

```html
<!DOCTYPE html>
<html lang="en">
<head>
<meta charset="utf-8">
<title>PKRT Leadership Groups – Office Poster</title>
<link href="https://fonts.googleapis.com/css2?family=Montserrat:wght@400;500;700&family=Playfair+Display:wght@400&display=swap" rel="stylesheet">
<style>
  :root {
    --backdrop: #dedede;
    --gold: #b9a06a;
    --ink: #0f0f0f;
    --paper-text: #ffffff;
    --rule: rgba(185, 160, 106, 0.75);
  }
  * { margin: 0; padding: 0; box-sizing: border-box; }
  html, body {
    width: 1200px; height: 1200px; overflow: hidden;
    background: var(--backdrop);
  }
  .poster {
    position: absolute; left: 210px; top: 50px;
    width: 780px; height: 1100px;
    background: var(--gold);
    padding: 11px;
  }
  .poster-inner {
    position: relative; width: 100%; height: 100%;
    background: var(--ink);
    color: var(--paper-text);
    font-family: "Montserrat", sans-serif;
  }
  .brand {
    position: absolute; top: 38px; left: 0; right: 0;
    display: flex; justify-content: center; align-items: center; gap: 12px;
  }
  .brand-mark { width: 14px; height: 14px; background: var(--paper-text); }
  .brand-name {
    font-weight: 500; font-size: 22px; letter-spacing: 5px;
    color: var(--paper-text); text-transform: uppercase;
  }
  .framed {
    position: absolute; left: 25px; width: 706px;
    border: 1px solid var(--rule);
  }
  .mission { top: 132px; height: 334px; }
  .frame-label {
    position: absolute; top: -11px; left: 50%; transform: translateX(-50%);
    background: var(--ink); padding: 0 13px;
    font-size: 20px; line-height: 22px; letter-spacing: 5px;
    color: var(--gold); white-space: nowrap;
  }
  .mission-statement {
    position: absolute; top: 32px; left: 20px; right: 20px;
    font-family: "Playfair Display", serif; font-weight: 400;
    font-size: 45px; line-height: 55.5px; text-align: center;
    color: var(--paper-text);
  }
  .section-rule {
    position: absolute; left: 0; right: 0; height: 1px; background: var(--rule);
  }
  .section-rule.upper { top: 493px; }
  .section-rule.lower { top: 974px; }
  .feedback-heading {
    position: absolute; top: 527px; left: 0; right: 0; text-align: center;
  }
  .feedback-kicker {
    font-size: 20px; letter-spacing: 5.5px; color: var(--gold); line-height: 26px;
  }
  .feedback-title {
    margin-top: 8px;
    font-weight: 700; font-size: 27px; color: var(--gold); line-height: 30px;
  }
  .testimonials { top: 617px; height: 330px; border-top: none; }
  .testimonials-top {
    position: absolute; top: 0; left: -1px; right: -1px; height: 1px;
  }
  .testimonials-top span {
    position: absolute; top: 0; height: 1px; background: var(--rule);
  }
  .quote-mark {
    position: absolute;
    font-family: "Playfair Display", serif; font-size: 64px; line-height: 1;
    color: var(--gold); transform: translateX(-50%);
  }
  .quote {
    position: absolute; text-align: center;
    font-size: 18.5px; line-height: 27px; color: var(--paper-text);
  }
  .quote.left { left: 18px; width: 300px; top: 22px; }
  .quote.right { left: 388px; width: 300px; top: 22px; }
  .quote.wide { left: 20px; right: 20px; top: 264px; }
  .column-divider {
    position: absolute; left: 353px; top: 41px; width: 1px; height: 130px;
    background: var(--rule);
  }
  .regions {
    position: absolute; top: 1012px; left: 0; right: 0; text-align: center;
    font-size: 18.5px; letter-spacing: 0.3px; color: var(--paper-text);
  }
  .site {
    position: absolute; top: 1053px; left: 0; right: 0;
    display: flex; justify-content: center; align-items: center; gap: 12px;
  }
  .site-line { width: 118px; height: 1px; background: var(--rule); }
  .site-url {
    font-weight: 700; font-size: 18.5px; letter-spacing: 4px; color: var(--paper-text);
  }
</style>
</head>
<body>
  <main class="poster">
    <div class="poster-inner">
      <header class="brand">
        <span class="brand-mark"></span>
        <span class="brand-name">PKRT Leadership Groups</span>
      </header>

      <section class="framed mission">
        <h2 class="frame-label">OUR CORE MISSION</h2>
        <p class="mission-statement">Helping good leaders to lead well through high-impact leadership support that blends genuine care with deep public sector nous.</p>
      </section>

      <div class="section-rule upper"></div>

      <div class="feedback-heading">
        <p class="feedback-kicker">VOICES FROM THE SECTOR</p>
        <h2 class="feedback-title">CLIENT FEEDBACK</h2>
      </div>

      <section class="framed testimonials">
        <div class="testimonials-top">
          <span style="left:0;width:139px"></span>
          <span style="left:202px;width:306px"></span>
          <span style="left:570px;width:138px"></span>
        </div>
        <span class="quote-mark" style="left:170px;top:-22px">”</span>
        <span class="quote-mark" style="left:540px;top:-22px">”</span>
        <p class="quote left">The best professional development I have undertaken in 30 years of public service. It has changed the way I think about my role and my leadership.</p>
        <div class="column-divider"></div>
        <p class="quote right">Participation has shaped how I approach my leadership skills and practice. The learnings from the groups are always in the back of my mind.</p>
        <span class="quote-mark" style="left:355px;top:210px">”</span>
        <p class="quote wide">The opportunity to share problems and hear perspectives from other colleagues is really helping me to do my job better.</p>
      </section>

      <div class="section-rule lower"></div>

      <p class="regions">COMMONWEALTH · NSW · VIC · QLD · SA · WA · ACT · NEW ZEALAND</p>
      <div class="site">
        <span class="site-line"></span>
        <span class="site-url">pkrt.com.au</span>
        <span class="site-line"></span>
      </div>
    </div>
  </main>
</body>
</html>
```